Verdant Orchard - Stationery Design Project

We need a stationary for our business. We grow roots and fruits in Central and South America, we import and distribute in FL, USA. We do fresh and frozen products.

Target Market(s)

Small and big supermarkets, wholesalers, traders, distributors, etc

Industry/Entity Type

Business

```html
<!DOCTYPE html>
<html lang="en">
<head>
<meta charset="utf-8">
<title>Verdant Orchard – Stationery</title>
<link href="https://fonts.googleapis.com/css2?family=Montserrat:wght@400;600&display=swap" rel="stylesheet">
<style>
  :root{
    --bg:#c3c3c3;
    --paper:#f4f4f4;
    --green:#4e5e30;
    --orange:#ea8a23;
    --ink:#3a3a3a;
    --muted:#6b6b6b;
    --screen:#8f8f8f;
    --window:#e6e6e6;
    --rule:#dcdcdc;
  }
  *{margin:0;padding:0;box-sizing:border-box}
  html,body{width:1200px;height:1000px;overflow:hidden}
  body{background:var(--bg);font-family:'Montserrat',Arial,sans-serif;color:var(--ink);position:relative}
  .piece{position:absolute;background:var(--paper);overflow:hidden}
  .brand{position:absolute;font-family:'Montserrat',Arial,sans-serif;font-weight:600;color:var(--green);
         text-transform:uppercase;letter-spacing:.04em;white-space:nowrap;line-height:1}
  .brand.on-green{color:var(--paper)}
  .brand.vertical{transform:rotate(-90deg);transform-origin:left top}
  .small{position:absolute;font-size:5px;line-height:1.6;color:var(--muted);white-space:nowrap}

  /* decorative band areas: soft gradient in the brand tones */
  .band{position:absolute;background:linear-gradient(to right,var(--orange) 0,var(--orange) 8%,var(--paper) 8%,var(--paper) 14%,var(--green) 14%)}
  .band.horizontal{background:linear-gradient(to bottom,var(--green) 0,var(--green) 70%,var(--orange) 70%)}
  .flap-rule{position:absolute;top:0;bottom:0;width:1px;background:var(--rule)}
  .stripe{position:absolute;width:3px}
  .stripe.green{background:var(--green)}
  .stripe.orange{background:var(--orange);width:2px}

  /* letterhead */
  .letterhead{left:241px;top:54px;width:316px;height:410px}
  .letterhead .band{right:0;top:0;bottom:0;width:44px}
  .letterhead .brand{left:62px;top:42px;font-size:16px}
  .letter-body{position:absolute;left:43px;top:92px;width:216px;font-size:5.6px;line-height:1.55;color:var(--ink)}
  .letter-body p{margin-bottom:7px}
  .letterhead .small{left:29px;top:362px}

  /* business cards */
  .card-front{left:580px;top:60px;width:132px;height:74px;background:var(--green)}
  .card-front .brand{left:22px;top:33px;font-size:8.5px}
  .card-back{left:580px;top:157px;width:132px;height:74px}
  .card-back .band{left:0;right:0;bottom:0;height:7px}
  .card-back .brand{left:6px;top:33px;font-size:6px}
  .card-back .details{position:absolute;right:7px;top:8px;text-align:right;font-size:3.6px;line-height:1.7;color:var(--green)}
  .card-back .details b{font-weight:600}

  /* app screen */
  .app-screen{left:756px;top:92px;width:82px;height:124px;background:var(--screen)}
  .app-tile{position:absolute;left:23px;top:44px;width:36px;height:36px;background:var(--green);border-radius:4px}

  /* envelopes */
  .envelope-back{left:580px;top:272px;width:318px;height:160px}
  .envelope-back .band{left:0;top:0;bottom:0;width:14px;background:linear-gradient(to right,var(--green) 0,var(--green) 60%,var(--paper) 60%,var(--paper) 75%,var(--orange) 75%)}
  .envelope-back .brand{left:26px;top:26px;font-size:11px}
  .envelope-front{left:624px;top:325px;width:322px;height:163px}
  .envelope-front .band{left:0;right:0;top:0;height:30px}
  .envelope-front .brand{left:10px;top:70px;font-size:11px}
  .envelope-front .window{position:absolute;left:198px;top:100px;width:110px;height:52px;background:var(--window);border-radius:6px}
  .envelope-front .small{left:16px;top:139px;font-size:4.5px}

  /* cd sleeve + disc */
  .cd-sleeve{left:362px;top:528px;width:181px;height:182px}
  .cd-sleeve .band{right:0;top:0;bottom:0;width:20px}
  .cd-sleeve .brand.front{left:42px;top:28px;font-size:10px}
  .cd-sleeve .brand.vertical{left:10px;top:166px;font-size:7px}
  .cd-disc{left:368px;top:745px;width:174px;height:174px;border-radius:50%}
  .cd-disc .band{left:0;right:0;bottom:0;height:58px}
  .cd-disc .hub{position:absolute;left:57px;top:57px;width:60px;height:60px;border-radius:50%;background:#ebebeb}
  .cd-disc .hole{position:absolute;left:74px;top:74px;width:26px;height:26px;border-radius:50%;background:var(--bg)}
  .cd-disc .brand{left:24px;top:42px;font-size:9.5px}

  /* folder */
  .folder{left:579px;top:542px;width:317px;height:406px}
  .folder .band{right:0;top:0;bottom:0;width:36px}
  .folder .brand.front{left:100px;top:50px;font-size:14px}
  .folder .brand.vertical{left:8px;top:375px;font-size:8px}
</style>
</head>
<body>

<!-- Letterhead -->
<section class="piece letterhead">
  <div class="band" role="img" aria-label="Green and orange brand band along the right edge"></div>
  <div class="brand">Verdant Orchard</div>
  <div class="letter-body">
    <p>Dear partner, thank you for your continued trust in our fresh and frozen produce. This letter confirms the details of our next seasonal shipment.</p>
    <p>Our roots and fruits are grown on partner farms across Central and South America, packed at origin and cooled within hours of harvest.</p>
    <p>Each lot is inspected on arrival at our Florida warehouse, then routed to supermarkets, wholesalers, traders and distributors on schedule. Frozen lines travel in dedicated cold trucks to keep quality steady from field to shelf.</p>
    <p>Please review the attached price list and confirm volumes for the coming quarter so we can reserve space.</p>
    <p>We look forward to growing together. Kind regards, the sales team.</p>
  </div>
  <div class="small">Grove Lane 715<br>Harbor City, FL 33101<br><br>+1 (305) 555 0142<br>hello@verdantorchard.com</div>
</section>

<!-- Business card front -->
<section class="piece card-front">
  <div class="brand on-green">Verdant Orchard</div>
</section>

<!-- Business card back -->
<section class="piece card-back">
  <div class="band horizontal" role="img" aria-label="Green and orange brand band along the bottom edge"></div>
  <div class="brand">Verdant Orchard</div>
  <div class="details"><b>Grove Lane 715</b><br>Harbor City, FL<br><br>+1 (305) 555 0142<br>+1 (305) 555 0143<br>hello@verdantorchard.com<br><br><b>Ana Morales</b></div>
</section>

<!-- App screen -->
<section class="piece app-screen">
  <div class="app-tile"></div>
</section>

<!-- Envelope back -->
<section class="piece envelope-back">
  <div class="band" role="img" aria-label="Green and orange brand band along the left edge"></div>
  <div class="brand">Verdant Orchard</div>
</section>

<!-- Envelope front -->
<section class="piece envelope-front">
  <div class="band horizontal" role="img" aria-label="Green and orange brand band across the flap"></div>
  <div class="brand">Verdant Orchard</div>
  <div class="window"></div>
  <div class="small">+1 (305) 555 0142<br>hello@verdantorchard.com</div>
</section>

<!-- CD sleeve -->
<section class="piece cd-sleeve">
  <div class="flap-rule" style="left:34px"></div>
  <div class="stripe green" style="left:17px;top:8px;height:102px"></div>
  <div class="stripe orange" style="left:22px;top:8px;height:102px"></div>
  <div class="band" role="img" aria-label="Green and orange brand band along the right edge"></div>
  <div class="brand front">Verdant Orchard</div>
  <div class="brand vertical">Verdant Orchard</div>
</section>

<!-- CD disc -->
<section class="piece cd-disc">
  <div class="band horizontal" role="img" aria-label="Green and orange brand band across the lower disc"></div>
  <div class="hub"></div>
  <div class="hole"></div>
  <div class="brand">Verdant Orchard</div>
</section>

<!-- Presentation folder -->
<section class="piece folder">
  <div class="flap-rule" style="left:31px"></div>
  <div class="stripe green" style="left:14px;top:18px;height:292px"></div>
  <div class="stripe orange" style="left:21px;top:18px;height:282px"></div>
  <div class="band" role="img" aria-label="Green and orange brand band along the right edge"></div>
  <div class="brand front">Verdant Orchard</div>
  <div class="brand vertical">Verdant Orchard</div>
</section>

</body>
</html>
```